Hurricane Damage Public Adjuster Billboard

I have created several projects with you and have several great designs. I need to format them into a Billboard for upcoming Hurricane Season. Need done in a month. Im also in process of getting an eye catching and easy to remember 800# Vanity phone number like Call 800-Stormsafe or 800- Need Help? My included past Pixel Bazaar projects will give you an idea of what colors, schemes, and designs I gravitate towards. 3 past Design projects were 1) 2 Logos where I picked the 1st place and the 2nd place and 2) Index Card where I picked the winner as the Index Card and the 2nd place as a Post Card. Point is, I will pick and pay for 2 winners if they're good. This should help to sweeten the pot. Also, please look at my website for ideas that I like:

www.CedarlineClaimHelp.com
I want people to feel that I am the best and highest. Level.

I've been getting a lot of quick half effort designs basically cut & pasting my previous projects. Please don't rush and take your time to be creative. A an example, my Biggest Competitor is Tamarack Public Adjusting. Their colors are Black and Gold while mine are Blue, White, and Black with a highlight of Orange if possible. I JUST imported a picture of their BillBoard. I need mine better and BLOW AWAY THEIRS. Terms like "Don't be Victimized Twice ?, Don't let the Hurricane Ruin your Life?". "Get Fairly Paid & Move On" "Our Clients Claims are VIP?
Updates

I'm getting a lot of quick half effort ones. I'd rather you take your time and really put some thoughts and effort into it. My Biggest Competitor is Tamarack Public Adjusting. They have black & gold colors, while I have Blue, Black, and white.

It needs to blow theirs away. I have imported their Billboard for comparative purposes.

Guy's,
I'll make it easier for you in what I'm looking for. Please look at the Tamarack Billboard picture attached.

1) Put my "Blue Shield" to the left, replacing their logo
2) change color patterns from their (Black, Gold, White) to my color schemes of (Black, Blue, White)
3) I want to see my name where their is:

THE
Cedarline Claim Help
EXPERT & LOCAL Public Adjusters
"FOR THE POLICYHOLDER!!"

4) to the right, add the A+Rated logo and QRT+ Accredited logo, 5 Star Zorvex Rated logo, 5 Start PORCHLINK Highly Rated logo, etc..

5) the right side is where you can be creative as I will not have a picture of me there.

"20+ Years of Experience, Recovering Millions for our VIP Clients"

"Your Best, Locally-Based Private Adjuster & Advocate'
"FOR THE POLICYHOLDER!!"

"Don't be victimized Twice!!"

"Don't let the Hurricane Ruin Your Life!!"

This should really help. Also, refer to my website, maybe a couple testimonial fillers?

Thanks all,

marcus@CedarlineClaimHelp.com

Just imported a few awards that would look great to the right side with all the other 5 Star Ratings and accolades.
This right section could be titled like zmy Website:

5 Star Reviews, Ratings & Awards:
4-5 Logos underneath?

Target Market(s)

Coastal place where a Hurricane 🌀 🌀 Hits

Industry/Entity Type

Hurricane Public Insurance Adjuster

Font styles to use
Sans Serif
Other font styles liked:
• Zurich fonts

Colors
0054AA
0677BA
7BADD7
CADEEF
E8F1F8
EE7325
F08F49
F5BC92
FAE3D3
FDF4ED

Requirements
Must have
• Use my past project logos, colors, and schemes to create eye grabbing BillBoard
Nice to have
Should not have
• Not be too busy, must be Easy to Read, Eye Catchy

```html
<!DOCTYPE html>
<html lang="en">
<head>
<meta charset="utf-8">
<title>Cedarline Claim Help – Hurricane Season Billboard</title>
<link rel="stylesheet" href="https://fonts.googleapis.com/css2?family=Montserrat:wght@400;500;600;700;800;900&family=Oswald:wght@500;600&display=swap">
<style>
  :root {
    --canvas: #45454d;
    --navy-deep: #060b1c;
    --navy: #0f2357;
    --storm-blue: #1f49a8;
    --brand-blue: #0677ba;
    --sky-blue: #2fa8ef;
    --mist: #e8f1f8;
    --white: #ffffff;
    --black: #000000;
    --orange: #ee7325;
    --orange-soft: #f08f49;
    --rating-red: #e52b2b;
    --star-gold: #f5bc32;
    --badge-teal: #0c6d8c;
  }
  * { margin: 0; padding: 0; box-sizing: border-box; }
  html, body { width: 1166px; height: 1200px; overflow: hidden; }
  body { background: var(--canvas); font-family: "Montserrat", sans-serif; position: relative; }

  .billboard {
    position: absolute; left: 33px; top: 440px;
    width: 1100px; height: 321px; overflow: hidden;
    background: var(--black);
  }
  .billboard__sky {
    position: absolute; left: 0; top: 0; width: 1100px; height: 240px;
    background:
      radial-gradient(ellipse 420px 200px at 90px 40px, rgba(232,241,248,.95), rgba(232,241,248,0) 70%),
      linear-gradient(100deg, #c9d3df 0%, #5b6f93 22%, var(--navy) 45%, var(--storm-blue) 75%, #1a3c93 100%);
  }
  .billboard__sky::after {
    content: ""; position: absolute; left: 0; bottom: 0; width: 100%; height: 70px;
    background: linear-gradient(to bottom, rgba(6,11,28,0), var(--navy-deep));
  }
  .hero-photo {
    position: absolute; left: 862px; top: 0; width: 190px; height: 240px;
    background: radial-gradient(ellipse 90px 120px at 95px 150px, #b9c9e2, rgba(120,150,200,.35) 70%, rgba(31,73,168,0));
  }

  .brand-mark {
    position: absolute; left: 58px; top: 88px; width: 150px;
    display: flex; flex-direction: column; align-items: center; gap: 10px;
  }
  .brand-mark__square { width: 44px; height: 44px; background: var(--sky-blue); }
  .brand-mark__name {
    font-weight: 800; font-size: 17px; line-height: 1.15; color: var(--sky-blue);
    text-align: center; text-transform: uppercase;
  }

  .title-block { position: absolute; left: 256px; top: 30px; width: 340px; color: var(--white); }
  .title-block__the {
    display: flex; align-items: center; gap: 4px; height: 34px;
    font-family: "Oswald", sans-serif; font-weight: 600; font-size: 34px;
  }
  .title-block__the::before, .title-block__the::after {
    content: ""; height: 2px; background: var(--white); flex: 1;
  }
  .title-block__name-top { font-weight: 900; font-size: 36px; line-height: 40px; letter-spacing: .5px; }
  .title-block__name-main { font-weight: 900; font-size: 46px; line-height: 48px; letter-spacing: .5px; }
  .title-block__tagline { font-weight: 500; font-size: 18px; margin-top: 3px; }
  .title-block__policyholder { font-weight: 600; font-size: 23.5px; color: var(--orange); margin-top: 2px; }
  .title-block__email { font-size: 11.5px; letter-spacing: 2px; margin-top: 2px; font-weight: 500; }

  .divider { position: absolute; left: 611px; top: 100px; width: 2px; height: 64px; background: rgba(255,255,255,.7); }

  .call-out { position: absolute; left: 651px; top: 90px; color: var(--white); }
  .call-out__headline { font-weight: 700; font-size: 22px; line-height: 25px; letter-spacing: .3px; }
  .call-out__tag {
    display: inline-block; margin-top: 15px; padding: 0 6px;
    background: var(--orange); color: var(--navy-deep);
    font-family: "Oswald", sans-serif; font-weight: 600; font-size: 14px; line-height: 18px;
  }
  .call-out__phone {
    display: flex; align-items: center; gap: 4px;
    font-family: "Oswald", sans-serif; font-weight: 600; font-size: 32px; line-height: 38px;
  }

  .slogan-band {
    position: absolute; left: 0; top: 240px; width: 1100px; height: 34px;
    background: var(--white); border: 2px solid var(--orange);
    display: flex; align-items: center; justify-content: center;
    font-weight: 900; font-size: 26px; letter-spacing: 1.3px; color: var(--black);
  }

  .footer-bar {
    position: absolute; left: 0; top: 274px; width: 1100px; height: 47px;
    display: flex; align-items: center; justify-content: space-between; padding: 0 42px 0 45px;
  }
  .footer-bar__site { color: var(--white); font-weight: 500; font-size: 23px; letter-spacing: .6px; }
  .ratings { display: flex; align-items: center; gap: 18px; }
  .rating-zorvex { display: flex; flex-direction: column; align-items: center; line-height: 1; }
  .rating-zorvex__name { color: var(--mist); font-weight: 500; font-size: 14px; }
  .rating-zorvex__stars { color: var(--star-gold); font-size: 9px; letter-spacing: 1px; }
  .rating-porchlink {
    display: flex; align-items: center; gap: 4px; height: 22px; padding: 0 5px 0 0;
    border: 1px solid var(--orange-soft);
  }
  .rating-porchlink__num {
    background: var(--orange); color: var(--white); font-weight: 800; font-size: 15px;
    width: 18px; height: 20px; display: flex; align-items: center; justify-content: center;
  }
  .rating-porchlink__name { color: var(--orange-soft); font-weight: 600; font-size: 10px; }
  .rating-grade { color: var(--rating-red); font-weight: 700; font-size: 22px; }
  .accreditation-badge { width: 72px; height: 26px; background: var(--badge-teal); border: 1px solid var(--mist); border-radius: 2px; }
</style>
</head>
<body>
  <section class="billboard" aria-label="Cedarline Claim Help hurricane season billboard">
    <div class="billboard__sky" role="img" aria-label="Dark stormy sky with lightning"></div>
    <div class="hero-photo" role="img" aria-label="Stressed homeowner at a laptop under a lightning strike"></div>

    <div class="brand-mark">
      <span class="brand-mark__square"></span>
      <span class="brand-mark__name">Cedarline Claim Help</span>
    </div>

    <div class="title-block">
      <div class="title-block__the">THE</div>
      <div class="title-block__name-top">CEDARLINE</div>
      <div class="title-block__name-main">CLAIM HELP</div>
      <div class="title-block__tagline">EXPERT &amp; LOCAL Public Adjusters</div>
      <div class="title-block__policyholder">FOR THE POLICYHOLDER</div>
      <div class="title-block__email">marcus@CedarlineClaimHelp.com</div>
    </div>

    <div class="divider"></div>

    <div class="call-out">
      <div class="call-out__headline">DON'T LET THE<br>HURRICANE RUIN<br>YOUR LIFE</div>
      <div class="call-out__tag">CONTACT NOW</div>
      <div class="call-out__phone">
        <svg width="12" height="24" viewBox="0 0 12 24" aria-hidden="true">
          <path d="M9 2 C4 3 2 8 2 12 C2 16 4 21 9 22 L10 17 C7 16 6 14 6 12 C6 10 7 8 10 7 Z" fill="#ffffff"/>
        </svg>
        (555) 014-2290
      </div>
    </div>

    <div class="slogan-band">YOUR BEST, LOCALLY-BASED PRIVATE ADJUSTER &amp; ADVOCATE</div>

    <footer class="footer-bar">
      <span class="footer-bar__site">www.CedarlineClaimHelp.com</span>
      <div class="ratings">
        <div class="rating-zorvex">
          <span class="rating-zorvex__name">Zorvex</span>
          <span class="rating-zorvex__stars">★★★★★</span>
        </div>
        <div class="rating-porchlink">
          <span class="rating-porchlink__num">5</span>
          <span class="rating-porchlink__name">STARS PORCHLINK</span>
        </div>
        <span class="rating-grade">A+ Rating</span>
        <span class="accreditation-badge" aria-label="Accreditation badge"></span>
      </div>
    </footer>
  </section>
</body>
</html>
```